Need a powerful, eye-catching book cover design for a Public Relations book for Lawyers.

We need a beautiful, elegant, and professional cover for a public relations book. We’ll be selling this both to (1) creative, experienced legal marketers, and (2) conservative lawyers. It must grab their attention visually, and have a bold, easy to read headline. The cover image may wrap around to the back cover.SIZE: 6 x 9” 100 pagesTITLE: The Ultimate Public Relations Handbook for LawyersSUBHEAD: Make millions using media and the InternetCO-AUTHORSRoss Fishman, JDJohn HellermanInclude a CALLOUT quote: “The definitive PR book. Simple and powerful.” – Tad Lurvey, SkaddenGRAPHICS:You may use one of the attached photos, crop or flip them however you’d like, or use something else entirely. DESCRIPTION for the back cover:Why do some law firms have the best reputations or command the highest hourly rates? Why are some the go-to firms or thought leaders in particular specialties? Why are your competitors in the media more than you? Two words: Public relations. The co-authors are known worldwide as leaders in public relations, legal marketing, and branding. Neil Stamford is called, “A PR Guru.” Bar Ledger magazine wrote ““Many people consider Dale Warbeck to be the nation’s foremost expert on law firm marketing.”Tad Lurvey built Brommick into the first firm to generate $1 billion in revenue. Yvonne Pelstrup is the nation’s go-to lawyer for women’s issues. Your home town’s top PI lawyer gets the first look at the biggest cases. Why? Strategic, intentional, effective PR. Are you tired of toiling in anonymity? Want to earn the attention of reporters and editors who can build your credentials and reputation for expertise? Wouldn’t it be nice to have more clients begging you to represent them because they heard you were the best in town? That is what public relations is designed to do. Want to get more respect, earn more clients, and charge higher rates? Get known as a thought leader in a specialty practice or industry? Public relations could be your most-important marketing tool. And this book will teach you precisely how. Ready to catapult your practice to new heights? Take a deep breath and dive in….

Target Market(s)

1. Creative marketing professionals
2. Conservative 40-year-old lawyers

Industry/Entity Type

Legal

Font styles to use
Serif

Requirements
Must have
• Want a simple, bold, eye catching design conveying professionalism and quality. This is a practical, how-to book. We need a simple design and strong headline that will work well at a small thumbnail size on Zelbora.
Nice to have
• Perhaps the microphone could wrap around the cover? A tight crop of a microphone that creates an abstract could work. Let's create something memorable.

```html
<!DOCTYPE html>
<html lang="en">
<head>
<meta charset="utf-8">
<title>The Complete Press Outreach Manual for Attorneys – Cover Spread</title>
<link href="https://fonts.googleapis.com/css2?family=Open+Sans:ital,wght@0,300;0,400;0,600;1,400&family=Roboto+Condensed:wght@700&family=Great+Vibes&display=swap" rel="stylesheet">
<style>
  :root {
    --page-bg: #e9e6e1;
    --cover-black: #050708;
    --ink-white: #ffffff;
    --ink-soft: #d9dee0;
    --teal-glow: #2b5a60;
    --teal-deep: #10262a;
    --rule: #6f8a90;
  }
  * { margin: 0; padding: 0; box-sizing: border-box; }
  html, body {
    width: 913px; height: 1200px; overflow: hidden;
    background: var(--page-bg);
  }
  .spread {
    position: absolute; left: 27px; top: 283px;
    width: 860px; height: 633px;
    background: var(--cover-black);
    font-family: "Open Sans", sans-serif;
    color: var(--ink-white);
    overflow: hidden;
  }
  .mic-photo {
    position: absolute; left: 400px; top: 120px;
    width: 460px; height: 470px;
    background:
      radial-gradient(ellipse 110px 130px at 247px 255px, rgba(70,120,126,.85), rgba(30,62,68,.55) 55%, transparent 100%),
      radial-gradient(circle 22px at 30px 100px, rgba(60,90,95,.35), transparent),
      radial-gradient(circle 22px at 80px 100px, rgba(60,90,95,.3), transparent),
      radial-gradient(circle 24px at 135px 100px, rgba(60,90,95,.3), transparent),
      radial-gradient(ellipse 200px 260px at 247px 260px, var(--teal-deep), transparent 100%);
  }
  .back-copy {
    position: absolute; left: 63px; top: 80px; width: 296px;
    font-size: 8.6px; line-height: 13.6px; color: var(--ink-soft);
    text-align: justify;
  }
  .back-copy p { text-indent: 14px; margin-bottom: 13.6px; }
  .front { position: absolute; left: 430px; top: 0; width: 430px; height: 633px; }
  .title { position: absolute; left: 0; width: 100%; text-align: center; font-weight: 400; }
  .title-article { position: absolute; left: 195px; top: 44px; font-size: 21px; }
  .title-main { position: absolute; left: 73px; top: 58px; font-size: 62px; line-height: 1; letter-spacing: -.5px; }
  .title-middle { position: absolute; left: 76px; top: 122px; font-size: 19px; }
  .title-for { position: absolute; left: 296px; top: 112px; font-family: "Great Vibes", cursive; font-size: 34px; }
  .title-last { position: absolute; left: 74px; top: 136px; font-size: 48px; letter-spacing: -.3px; }
  .rule {
    position: absolute; left: 80px; width: 270px; height: 1px;
    background: linear-gradient(90deg, transparent, var(--rule), transparent);
  }
  .subhead {
    position: absolute; left: 0; width: 430px; top: 226px; text-align: center;
    font-family: "Roboto Condensed", sans-serif; font-weight: 700; font-size: 12.5px; letter-spacing: .4px;
  }
  .quote-mark {
    position: absolute; left: 207px; top: 508px; width: 14px; height: 14px;
    border-radius: 50%; background: var(--ink-white); color: var(--cover-black);
    font-size: 10px; line-height: 15px; text-align: center; font-weight: 600;
  }
  .callout {
    position: absolute; left: 0; width: 430px; top: 531px; text-align: center;
    font-style: italic; font-size: 10.5px;
  }
  .callout-source {
    position: absolute; left: 0; width: 430px; top: 546px; text-align: center; font-size: 9px;
  }
  .authors {
    position: absolute; left: 0; width: 430px; top: 590px; text-align: center;
    font-family: "Roboto Condensed", sans-serif; font-weight: 700; font-size: 12.5px; letter-spacing: .4px;
  }
</style>
</head>
<body>
<div class="spread">
  <div class="mic-photo" role="img" aria-label="Close-up photograph of a stage microphone lit in teal against a dark background, with soft bokeh lights wrapping toward the back cover"></div>

  <div class="back-copy">
    <p>Why do some law firms have the best reputations or command the highest hourly rates? Why are some the go-to firms or thought leaders in particular specialties?</p>
    <p>Why are your competitors in the media more than you? Two words: Public relations. The co-authors are known worldwide as leaders in public relations, legal marketing, and branding. Neil Stamford is called, “A PR Guru.” Bar Ledger magazine wrote ““Many people consider Dale Warbeck to be the nation’s foremost expert on law firm marketing.”Tad Lurvey built Brommick into the first firm to generate $1 billion in revenue. Yvonne Pelstrup is the nation’s go-to lawyer for women’s issues. Your home town’s top PI lawyer gets the first look at the biggest cases. Why? Strategic, intentional, effective PR. Are you tired of toiling in anonymity? Want to earn the attention of reporters and editors who can build your credentials and reputation for expertise? Wouldn’t it be nice to have more clients begging you to represent them because they heard you were the best in town?</p>
    <p>That is what public relations is designed to do. Want to get more respect, earn more clients, and charge higher rates? Get known as a thought leader in a specialty practice or industry? Public relations could be your most-important marketing tool. And this book will teach you precisely how. Ready to catapult your practice to new heights? Take a deep breath and dive in….</p>
  </div>

  <div class="front">
    <h1 class="book-title">
      <span class="title-article">the</span>
      <span class="title-main">Complete</span>
      <span class="title-middle">Press Outreach Manual</span>
      <span class="title-for">for</span>
      <span class="title-last">Attorneys</span>
    </h1>
    <div class="rule" style="top:211px"></div>
    <div class="subhead">Make millions using media and the Internet</div>
    <div class="rule" style="top:260px"></div>

    <div class="rule" style="top:515px;left:60px;width:310px"></div>
    <div class="quote-mark">“</div>
    <p class="callout">The definitive PR book. Simple and powerful.”</p>
    <p class="callout-source">– Tad Lurvey, Brommick</p>
    <div class="rule" style="top:570px;left:60px;width:310px"></div>
    <p class="authors">CO-AUTHORS Dale Warbeck, JD Neil Stamford</p>
  </div>
</div>
</body>
</html>
```